Marwell Herd Services concrete grooving services flyer design

Marwell Herd Services offers 4 different grooving options:

DEEP GROOVING
, ideal for Safety & Efficiency
Our hugely popular deep straight line grooving, long lasting, minimal hoof wear,

Create safe and secure flooring, cows walk without hesitation

Achieve groove spacing for optimal hoof function, reduce hoof trauma

Ideal grooves to new concrete or surfaces with little to no pattern or previous grooving

Ideal groove pattern as promoted by The pasturewide programme

MINI GROOVING,
Smaller dimensions Ideal option for heifer housing and high activity areas such as parlours and handling areas

An ideal solution for regaining traction on old previous grooving that has lost its traction without loosing stability

Plaining

smoothing down rough concrete with previous aggressive grooving or patterns to reduce hoof trauma & wear

SENSOR PLATE SINKING

sinking sensor plates for automated machines below surface level preventing accidental damage & wear

```html
<!DOCTYPE html>
<html lang="en">
<head>
<meta charset="utf-8">
<title>Marwell Herd Services – Concrete Grooving Services Flyer</title>
<link href="https://fonts.googleapis.com/css2?family=Oswald:wght@300;400;500;600&display=swap" rel="stylesheet">
<style>
  :root {
    --page-bg: #ececec;
    --brand-yellow: #fecf00;
    --brand-green: #04632b;
    --brand-black: #0b0b0b;
    --white: #ffffff;
    --bullet-green: #4fb848;
    --photo-light: #d9d9d6;
    --photo-mid: #9b9890;
    --photo-dark: #5e4d38;
  }
  * { margin: 0; padding: 0; box-sizing: border-box; }
  html, body {
    width: 1200px; height: 1000px; overflow: hidden;
    background: var(--page-bg);
    font-family: "Oswald", sans-serif;
  }
  .flyer {
    position: absolute; left: 416px; top: 85px;
    width: 392px; height: 830px; overflow: hidden;
    background: var(--brand-yellow);
  }
  .flyer-shapes { position: absolute; inset: 0; }
  .brand {
    position: absolute; left: 44px; top: 40px; width: 151px;
    text-align: center; color: var(--brand-black); font-weight: 500;
  }
  .brand-mark {
    width: 66px; height: 66px; margin: 0 auto 8px;
    border: 2px solid var(--brand-black); border-radius: 50%;
  }
  .brand-name { font-size: 30px; line-height: 1; letter-spacing: 1px; }
  .brand-sub { font-size: 10.5px; line-height: 1.3; letter-spacing: 1.2px; }
  .headline {
    position: absolute; left: 54px; top: 540px;
    color: var(--white); text-transform: uppercase; line-height: 0.98;
  }
  .headline-strong { display: block; font-size: 66px; font-weight: 600; letter-spacing: -0.5px; }
  .headline-light { display: block; font-size: 66px; font-weight: 300; letter-spacing: -0.5px; }
  .service-list {
    position: absolute; left: 56px; top: 742px;
    list-style: none;
    display: grid; grid-template-columns: 139px auto; row-gap: 6px;
    color: var(--brand-yellow); font-size: 16px; font-weight: 400; line-height: 21px;
  }
  .service-list li { position: relative; padding-left: 11px; white-space: nowrap; }
  .service-list li::before {
    content: ""; position: absolute; left: 0; top: 6px;
    border-left: 8px solid var(--bullet-green);
    border-top: 5px solid transparent; border-bottom: 5px solid transparent;
  }
</style>
</head>
<body>
  <main class="flyer">
    <svg class="flyer-shapes" width="392" height="830" viewBox="0 0 392 830" aria-hidden="false">
      <defs>
        <linearGradient id="barnPhotoTone" x1="0" y1="1" x2="1" y2="0">
          <stop offset="0" stop-color="var(--photo-light)"/>
          <stop offset="0.45" stop-color="var(--photo-mid)"/>
          <stop offset="0.75" stop-color="var(--photo-dark)"/>
          <stop offset="1" stop-color="var(--photo-mid)"/>
        </linearGradient>
      </defs>
      <polygon class="barn-photo" role="img" aria-label="Photo of a grooved concrete barn floor under a steel-framed roof"
               points="0,245 392,75 392,830 0,830" fill="url(#barnPhotoTone)"/>
      <polygon class="logo-panel" points="44,0 195,0 195,151 44,217" fill="var(--white)"/>
      <polygon class="black-wedge" points="0,450 230,526 0,627" fill="var(--brand-black)"/>
      <polygon class="green-base" points="0,627 392,455 392,830 0,830" fill="var(--brand-green)"/>
      <polygon class="green-tint" points="230,526 392,455 392,600 300,560" fill="var(--brand-green)" opacity="0.55"/>
    </svg>

    <div class="brand">
      <div class="brand-mark"></div>
      <div class="brand-name">MARWELL</div>
      <div class="brand-sub">HERD SERVICES</div>
    </div>

    <h1 class="headline">
      <span class="headline-strong">Concrete</span>
      <span class="headline-strong">Grooving</span>
      <span class="headline-light">Services</span>
    </h1>

    <ul class="service-list">
      <li>Deep Grooving</li>
      <li>Mini Grooving,</li>
      <li>Plaining</li>
      <li>Sensor Plate Sinking</li>
    </ul>
  </main>
</body>
</html>
```